Whitening Pen artwork design

Whitening Pens with silkscreen printing:
sample: https://www.shopvarnel.com/Korimo-Whitening-Carbamide-Sensitivity-Travel-Friendly/dp/Q48T2K9X5R/ref=sr_1_5?dchild=1&keywords=whitening+pen&qid=1615425398&sr=8-5

inside the writing:
"teeth whitening pen " change to "FARO WHITENING PEN"
"logo" change to our logo

requirements:
Inches: 1.77" wide x 1.57" around
CM: 4.5cm wide x 4cm around

See attached file Generic Pen Artwork Placement Silkscreen – this is not a template, just a guideline, refer to the exact sizing above

- An "identifying marker" is required: Teeth Whitening Pen or Teeth Whitening Gel (for example)

-We require PDF files created to print ready specifications. Color images should be down-sampled to 300DPI

-Please provide us your Hueledger color reference for the color used in your artwork

https://www.hueledger.com/color-finder#/pick?hueBook=hueSolidCoatedV3M2

-Please ensure that all fonts are embedded in the PDF document or make sure you convert fonts to outlines to prevent any issues with fonts (AI-Type-Create Outlines)

We will need your print ready artwork in a high resolution PDF file

```html
<!DOCTYPE html>
<html lang="en">
<head>
<meta charset="utf-8">
<title>Faro Whitening Pen – Silkscreen Artwork</title>
<link rel="stylesheet" href="https://fonts.googleapis.com/css2?family=Montserrat:wght@300;400;600&display=swap">
<style>
  :root {
    --ink-dark: #454a4f;
    --blush: #e7a89b;
    --paper: #ffffff;
    --guide-red: #e2323c;
    --rule-grey: #8a8a8a;
    --pen-clear: #eef1f6;
    --pen-shade: #c9cfdb;
  }
  html, body {
    margin: 0;
    padding: 0;
    width: 708px;
    height: 1200px;
    overflow: hidden;
    background: var(--paper);
  }
  .artboard {
    display: block;
    width: 708px;
    height: 1200px;
    font-family: "Montserrat", sans-serif;
  }
  .brand-name { font-family: "Montserrat", sans-serif; font-weight: 600; fill: var(--ink-dark); }
  .product-line { font-family: "Montserrat", sans-serif; font-weight: 300; fill: var(--blush); }
  .dimension-label { font-family: "Montserrat", sans-serif; font-weight: 400; fill: #111; font-size: 24px; }
  .brand-dot { fill: var(--blush); }
  .guide { stroke: var(--guide-red); stroke-width: 1; fill: none; }
  .outline { stroke: var(--rule-grey); stroke-width: 0.6; fill: none; }
  .label-edge { stroke: var(--blush); stroke-width: 0.6; fill: none; }
</style>
</head>
<body>
<svg class="artboard" viewBox="0 0 708 1200" xmlns="http://www.w3.org/2000/svg">
  <defs>
    <linearGradient id="penBody" x1="0" x2="1" y1="0" y2="0">
      <stop offset="0" stop-color="var(--pen-shade)"/>
      <stop offset="0.5" stop-color="var(--pen-clear)"/>
      <stop offset="1" stop-color="var(--pen-shade)"/>
    </linearGradient>
  </defs>

  <!-- Retail box front -->
  <g class="retail-box">
    <rect x="107" y="19" width="149" height="669" fill="var(--paper)" stroke="#dcdcdc" stroke-width="1.5"/>
    <rect x="107" y="19" width="51" height="669" fill="var(--ink-dark)"/>
    <text class="product-line" font-size="17" transform="translate(128 47) rotate(90)" textLength="619" lengthAdjust="spacingAndGlyphs">FARO WHITENING PEN · Professional Level Whitening Guaranteed</text>
    <circle class="brand-dot" cx="205" cy="157" r="22"/>
    <text class="brand-name" font-size="70" transform="translate(180 200) rotate(90)" textLength="430" lengthAdjust="spacingAndGlyphs">MIRAVO WHITE</text>
  </g>

  <!-- Pen mockups -->
  <g class="pen-mockups">
    <rect role="img" aria-label="Clear whitening pen with brush tip and printed brand label" x="280" y="29" width="64" height="654" rx="12" fill="url(#penBody)"/>
    <rect role="img" aria-label="Clear whitening pen with brush tip and printed brand label" x="370" y="29" width="64" height="654" rx="12" fill="url(#penBody)"/>
  </g>

  <!-- Single label artwork -->
  <g class="label-artwork">
    <rect class="label-edge" x="505" y="113" width="95" height="479"/>
    <circle class="brand-dot" cx="570" cy="172" r="18"/>
    <text class="brand-name" font-size="54" transform="translate(551 208) rotate(90)" textLength="337" lengthAdjust="spacingAndGlyphs">MIRAVO WHITE</text>
    <text class="product-line" font-size="24" transform="translate(516 214) rotate(90)" textLength="274" lengthAdjust="spacingAndGlyphs">FARO WHITENING PEN</text>
  </g>

  <!-- Circumference diagram -->
  <g class="diameter-guide">
    <circle class="outline" cx="401" cy="824" r="91"/>
    <line class="guide" x1="310" y1="824" x2="492" y2="824"/>
    <text class="dimension-label" x="405" y="857" text-anchor="middle">D=4cm</text>
  </g>

  <!-- Unrolled print area -->
  <g class="print-area">
    <rect class="outline" x="114" y="916" width="574" height="205"/>

    <g class="wrap-label" transform="translate(237 0)">
      <line class="label-edge" x1="0" y1="916" x2="0" y2="1121"/>
      <line class="label-edge" x1="41" y1="916" x2="41" y2="1121"/>
      <circle class="brand-dot" cx="28" cy="941" r="8"/>
      <text class="brand-name" font-size="26" transform="translate(19 955) rotate(90)" textLength="147" lengthAdjust="spacingAndGlyphs">MIRAVO WHITE</text>
      <text class="product-line" font-size="11" transform="translate(4 958) rotate(90)" textLength="118" lengthAdjust="spacingAndGlyphs">FARO WHITENING PEN</text>
    </g>
    <g class="wrap-label" transform="translate(381 0)">
      <line class="label-edge" x1="0" y1="916" x2="0" y2="1121"/>
      <line class="label-edge" x1="41" y1="916" x2="41" y2="1121"/>
      <circle class="brand-dot" cx="28" cy="941" r="8"/>
      <text class="brand-name" font-size="26" transform="translate(19 955) rotate(90)" textLength="147" lengthAdjust="spacingAndGlyphs">MIRAVO WHITE</text>
      <text class="product-line" font-size="11" transform="translate(4 958) rotate(90)" textLength="118" lengthAdjust="spacingAndGlyphs">FARO WHITENING PEN</text>
    </g>
    <g class="wrap-label" transform="translate(524 0)">
      <line class="label-edge" x1="0" y1="916" x2="0" y2="1121"/>
      <line class="label-edge" x1="41" y1="916" x2="41" y2="1121"/>
      <circle class="brand-dot" cx="28" cy="941" r="8"/>
      <text class="brand-name" font-size="26" transform="translate(19 955) rotate(90)" textLength="147" lengthAdjust="spacingAndGlyphs">MIRAVO WHITE</text>
      <text class="product-line" font-size="11" transform="translate(4 958) rotate(90)" textLength="118" lengthAdjust="spacingAndGlyphs">FARO WHITENING PEN</text>
    </g>

    <!-- Height dimension -->
    <line class="guide" x1="81" y1="916" x2="114" y2="916"/>
    <line class="guide" x1="81" y1="1121" x2="114" y2="1121"/>
    <line class="guide" x1="98" y1="916" x2="98" y2="1118"/>
    <text class="dimension-label" x="19" y="1026">4.5cm</text>

    <!-- Width dimension -->
    <line class="guide" x1="114" y1="1121" x2="114" y2="1154"/>
    <line class="guide" x1="688" y1="1121" x2="688" y2="1154"/>
    <line class="guide" x1="114" y1="1138" x2="688" y2="1138"/>
    <text class="dimension-label" x="400" y="1170" text-anchor="middle">12.5664cm (Pi=3.1416 x 4 cm)</text>
  </g>
</svg>
</body>
</html>
```